Brennick Holdings Business Cards

These are professional business cards that are for my family office.
Put fake emails and phone numbers as of now until I finalize those components. This family office controls my families investments, assets, and future. The cards should be professional.
..
.
.
.
I just uploaded another variation of a logo I would like to see as a business card to I am inbeteen which logo to use

Target Market(s)

business

Industry/Entity Type

business

Contact Information for Business Card

Professional, wealth related, finance related.

Requirements
Must have
• Logo

```html
<!DOCTYPE html>
<html lang="en">
<head>
<meta charset="utf-8">
<title>Brennick Holdings Business Cards</title>
<link href="https://fonts.googleapis.com/css2?family=Cinzel:wght@400;600&family=Crimson+Text:ital,wght@0,400;1,400&display=swap" rel="stylesheet">
<style>
  :root {
    --stage: #0e0e10;
    --card: #141824;
    --ink: #f4f4f4;
    --ink-muted: #9b9ca1;
    --rule: #4a4d57;
  }
  * { box-sizing: border-box; margin: 0; padding: 0; }
  html, body {
    width: 1200px; height: 963px; overflow: hidden;
    background: var(--stage);
  }
  .sheet {
    width: 1200px; height: 963px;
    display: flex; flex-direction: column; align-items: center; justify-content: center;
    gap: 56px;
  }
  .card {
    width: 700px; height: 400px;
    background: var(--card);
    position: relative;
    box-shadow: 0 18px 40px rgba(0,0,0,.55);
  }
  /* Front */
  .card-front { display: flex; flex-direction: column; align-items: center; justify-content: center; gap: 26px; }
  .brand-mark {
    width: 120px; height: 120px; border: 5px solid var(--ink); border-radius: 50%;
  }
  .brand-name {
    font-family: "Cinzel", serif; font-weight: 600; font-size: 40px;
    color: var(--ink); letter-spacing: 2px;
  }
  /* Back */
  .card-back { display: flex; flex-direction: column; align-items: center; justify-content: center; gap: 40px; }
  .contact-row { display: flex; align-items: center; gap: 22px; }
  .identity { text-align: right; }
  .person-name {
    font-family: "Cinzel", serif; font-size: 30px; color: var(--ink-muted); letter-spacing: 1px;
  }
  .person-role {
    font-family: "Crimson Text", serif; font-size: 22px; color: var(--ink); margin-top: 2px;
  }
  .divider { width: 1px; height: 92px; background: var(--rule); }
  .contact-list { list-style: none; display: flex; flex-direction: column; gap: 4px; }
  .contact-item {
    display: flex; align-items: center; gap: 10px;
    font-family: "Crimson Text", serif; font-size: 22px; color: var(--ink);
  }
  .contact-icon { width: 18px; height: 18px; flex: none; }
  .address {
    font-family: "Crimson Text", serif; font-size: 22px; color: var(--ink);
  }
</style>
</head>
<body>
<main class="sheet">
  <section class="card card-front" aria-label="Card front">
    <div class="brand-mark" aria-hidden="true"></div>
    <h1 class="brand-name">BRENNICK HOLDINGS</h1>
  </section>

  <section class="card card-back" aria-label="Card back">
    <div class="contact-row">
      <div class="identity">
        <p class="person-name">MARCUS ELLERY</p>
        <p class="person-role">Manager</p>
      </div>
      <div class="divider"></div>
      <ul class="contact-list">
        <li class="contact-item">
          <svg class="contact-icon" viewBox="0 0 20 20" aria-hidden="true"><rect x="2" y="9" width="16" height="9" rx="2" fill="#b8b9be"/><path d="M2 8c0-4 16-4 16 0v2h-4V8H6v2H2z" fill="#b8b9be"/></svg>
          123-456-2100
        </li>
        <li class="contact-item">
          <svg class="contact-icon" viewBox="0 0 20 20" aria-hidden="true"><rect x="1" y="4" width="18" height="12" rx="1" fill="#b8b9be"/><path d="M1 5l9 6 9-6" stroke="#141824" stroke-width="1.5" fill="none"/></svg>
          yourname@brennickmail.com
        </li>
        <li class="contact-item">
          <svg class="contact-icon" viewBox="0 0 20 20" aria-hidden="true"><circle cx="10" cy="10" r="8.5" fill="#b8b9be"/><path d="M10 1.5v17M1.5 10h17M10 1.5c-4 4-4 13 0 17M10 1.5c4 4 4 13 0 17" stroke="#141824" stroke-width="1.2" fill="none"/></svg>
          www.yourwebsite.com
        </li>
      </ul>
    </div>
    <p class="address">Your Address, City, State, Zip 0000</p>
  </section>
</main>
</body>
</html>
```